New Design for Accounting Firm

CLIENT NAME: Corvantis
CURRENT WEBSITE: www.corvantisgroup-example.com.au

CLIENTS THE CLIENT LIKES:
http://velmarook.example.se/
http://www.tralvexio.example.biz/index.php
http://www.brindlequo.example.co.uk/
http://www.nerovaskellintrust.example.org/

COLOUR THEMES:
Colour theme to reflect the logo, with a leaning to blue in Accounting & Audit sections and green in Super section.

LOOK AND FEEL:
The look and feel needs to reflect an accessible culture and contemporary sensibility while still communicating our experience and stability as a professional company.

ABOUT:
The concept of 'Corvantis' is integral to our identity. Definition: 'The connection of creative ideas from a group of diverse individuals, applied with the end aim of solving practical problems'. See ''About Us'' on our website for more.

OTHER DETAILS:
Our three divisions (and service areas within each division) must be easily navigated as they related to very different users of the site. Two client sign in sections (Accounting & Super) must be easily distinguished to avoid user confusion.

MENU STRUCTURE:
* About
- includes history, values, our people, community etc
* Accounting & Advisory
- About
- Services
- Tax & Accounting
- Business Advisory
- Family Wealth Management
- Client Sign In
- Calculators
* Audit & Assurance
- About
- Services
* Corvantis Super
- About
- Individuals
- Services
- Advisers
- Services
- Portal Sign In
- Calculators
* Careers
* Newsletters
* Contact

REQUIREMENTS:
- Layered PSD form home and content pages
- No coding required, we use our own CMS to insert XHTML files into.
Updates

Hi Guys,

The client has asked for a non-cliche'd images in the design. If you'd like to try again with some images that represent the business but aren't your standard boring accounting-looking people, then please do! Cliche is a killer in design - please pump some creativity in!

Cheers,
Ted.

Reason: GUYS - PLEASE LISTEN TO THESE COMMENTS - I'VE SAID THEM TWICE NOW AND PEOPLE ARE STILL POSTING PROJECTS WITH CLICHED AND OBVIOUS ACCOUTNING TYPE IMAGES. USE YOUR CREATIVITY AND POST A DESIGN THAT IS OUTSIDE THE BOX WITH REGARDS TO THE IMAGES YOU ARE USING.

Reason: I am waiting to hear back from the client on their decision.

```html
<!DOCTYPE html>
<html lang="en">
<head>
<meta charset="utf-8">
<title>Corvantis – Accountants, Advisers, Auditors and SMSF Specialists</title>
<link rel="stylesheet" href="https://fonts.googleapis.com/css2?family=Arimo:wght@400;700&family=Gelasio:ital,wght@1,400;1,500&family=Rokkitt:wght@400&display=swap">
<style>
  :root{
    --blue-dark:#044a77;
    --blue-mid:#0a78b6;
    --blue-title:#0d4f7c;
    --logo-blue:#1a6eaa;
    --green-top:#6cc82a;
    --green-accent:#a8ea6f;
    --green-footer:#5ec41b;
    --green-fold:#3f8c12;
    --sky:#e3f1f9;
    --panel:#e4f2fa;
    --text:#555b60;
    --nav-text:#4f5457;
    --line:#d3e3ec;
  }
  *{box-sizing:border-box;margin:0;padding:0}
  html,body{width:1200px;height:951px;overflow:hidden;background:#f4fafd}
  .page{
    position:relative;width:1230px;height:975px;
    transform:scale(0.97561);transform-origin:0 0;
    background:linear-gradient(#e3f1f9 0,#e6f3fa 360px,#eef7fb 600px,#f8fcfe 975px);
    font-family:Arimo,Arial,sans-serif;color:var(--text);
  }
  .top-line{position:absolute;left:0;top:0;width:100%;height:5px;background:var(--green-top)}
  .logo{position:absolute;left:150px;top:28px;display:flex;align-items:center;gap:14px}
  .logo-mark{width:44px;height:44px;background:var(--logo-blue);border-radius:3px}
  .logo-name{font-family:Arimo,Arial,sans-serif;font-size:56px;font-weight:400;color:var(--logo-blue);letter-spacing:-1px;line-height:1}
  .hero{position:absolute;left:0;top:130px;width:100%;height:233px;
    background:linear-gradient(#0b7cba,#07659f 45%,#044c79)}
  .nav{position:absolute;left:143px;top:107px;width:946px;height:47px;display:flex;
    background:linear-gradient(#ffffff,#eaf3f8);border:1px solid #cfe0ea;border-radius:5px;
    box-shadow:0 2px 4px rgba(0,40,70,.15);list-style:none}
  .nav li{display:flex;align-items:center;justify-content:center;font-weight:700;font-size:13px;color:var(--nav-text);border-right:1px solid #d6e3ea}
  .nav li:last-child{border-right:0}
  .headline{position:absolute;left:168px;top:198px;font-family:Rokkitt,Georgia,serif;font-size:31px;line-height:40px;color:#fff;letter-spacing:.2px}
  .headline em{font-style:normal;color:var(--green-accent)}
  .hero-art{position:absolute;left:792px;top:170px;width:285px;height:232px;border-radius:6px;
    background:linear-gradient(135deg,#9ddf5c 0%,#7fcf3e 50%,#dfe9ee 75%,#bcd4e4 100%);opacity:.95}
  .division{position:absolute;top:395px;width:300px}
  .division.middle-panel{background:linear-gradient(#eef7fc,#f3f9fc);box-shadow:0 0 14px rgba(120,160,190,.25);height:220px;top:390px;left:453px;width:327px;position:absolute}
  .division h2{display:flex;align-items:center;gap:8px;font-family:Gelasio,Georgia,serif;font-style:italic;font-weight:500;font-size:20px;color:var(--blue-title);height:40px;margin-top:12px}
  .division p{font-size:12px;line-height:20px;margin-top:14px}
  .division p.justify{text-align:justify}
  .tick{width:34px;height:30px;flex:none}
  .btn{position:absolute;top:157px;width:92px;height:28px;border:1px solid #c8cfd3;border-radius:4px;background:linear-gradient(#fff,#e9ecee);font-weight:700;font-size:12px;color:#444;display:flex;align-items:center;justify-content:center}
  .welcome{position:absolute;left:143px;top:616px;width:947px;height:310px;background:#fff;border:1px solid var(--line);border-radius:6px 6px 0 0}
  .welcome h1,.services h3{font-family:Gelasio,Georgia,serif;font-style:italic;font-weight:500;font-size:19px;color:var(--blue-title)}
  .welcome-body{position:absolute;left:27px;top:26px;width:587px}
  .dots{border-bottom:2px dotted #cdd6db;margin:6px 0 10px}
  .welcome-body p{font-size:12px;line-height:20px;margin-bottom:20px}
  .services{position:absolute;left:643px;top:13px;width:289px;height:261px;background:var(--panel);border-radius:6px;padding-top:10px}
  .services h3{text-align:center}
  .services .dots{margin:7px 0 14px}
  .services ul{list-style:none;padding-left:26px}
  .services li{display:flex;gap:18px;font-weight:700;font-size:12px;line-height:18px;color:#555;margin-bottom:12px}
  .services li::before{content:"";flex:none;width:0;height:0;margin-top:4px;border-left:6px solid var(--blue-mid);border-top:4px solid transparent;border-bottom:4px solid transparent}
  .footer{position:absolute;left:130px;top:917px;width:974px;height:46px;background:var(--green-footer);color:#fff;font-size:11px}
  .fold{position:absolute;top:903px;width:13px;height:14px;background:var(--green-fold)}
  .fold.left{left:130px;clip-path:polygon(100% 0,100% 100%,0 100%)}
  .fold.right{left:1090px;clip-path:polygon(0 0,0 100%,100% 100%)}
  .footer-links{position:absolute;left:30px;top:16px;display:flex;list-style:none}
  .footer-links li+li::before{content:"|";margin:0 9px}
  .copyright{position:absolute;left:722px;top:17px}
</style>
</head>
<body>
<div class="page">
  <div class="top-line"></div>
  <div class="hero"></div>

  <div class="logo"><span class="logo-mark"></span><span class="logo-name">Corvantis</span></div>

  <ul class="nav">
    <li style="width:84px">Home</li>
    <li style="width:88px">About</li>
    <li style="width:176px">Accounting &amp; Advisory</li>
    <li style="width:167px">Audit &amp; Assurance</li>
    <li style="width:131px">Corvantis Super</li>
    <li style="width:94px">Careers</li>
    <li style="width:117px">Newsletters</li>
    <li style="width:87px">Contact</li>
  </ul>

  <p class="headline">We offers the skills of <em>Accountants</em>,<br>Business Performance Advisers, Auditors and<br><em>Self Managed Super Fund</em> Specialists.</p>

  <div class="hero-art" role="img" aria-label="Illustration of a green document folder with a rising bar chart and arrow"></div>

  <div class="middle-panel division"></div>

  <section class="division" style="left:145px;width:288px">
    <h2><svg class="tick" viewBox="0 0 34 30"><path d="M3 16l6-4 6 7L29 2l3 3-16 22z" fill="#5cc41a"/></svg>Accounting and Advisory</h2>
    <p class="justify">Our Accounting and Advisory team - AG Corvantis Chartered Accountants - provide traditional accounting services and professional corporate and business advice.</p>
    <span class="btn" style="left:1px">Read More</span>
  </section>

  <section class="division" style="left:467px;width:292px">
    <h2><svg class="tick" viewBox="0 0 34 30"><path d="M3 16l6-4 6 7L29 2l3 3-16 22z" fill="#5cc41a"/></svg>Audit &amp; Assurance</h2>
    <p>While the number of firms providing audit services has decreased in recent years, Corvantis remain committed to audit as a core service.</p>
    <span class="btn" style="left:-1px">Read More</span>
  </section>

  <section class="division" style="left:799px;width:280px">
    <h2><svg class="tick" viewBox="0 0 34 30"><path d="M3 16l6-4 6 7L29 2l3 3-16 22z" fill="#5cc41a"/></svg>Corvantis Super</h2>
    <p>Corvantis Super is a specialist division formed in July 2009 to specifically service our rapidly growing SMSF client base, in response to the continual growth of the SMSF industry.</p>
    <span class="btn" style="left:0">Read More</span>
  </section>

  <main class="welcome">
    <div class="welcome-body">
      <h1>Welcome to Corvantis</h1>
      <div class="dots"></div>
      <p>Corvantis is a Tasmanian based firm which offers the skills of Accountants, Business Performance Advisers, Auditors and Self Managed Super Fund Specialists.</p>
      <p>our clients benefit from the application of specialist skills and systems, developed in relevant areas of expertise. At the same time, our teams are skilled at integrating their knowledge with the common goal of meeting our clients' comprehensive needs.</p>
      <p>Across the firm we deliver services in a wide range of industries; to individuals, businesses, corporations and financial advisers.</p>
    </div>
    <aside class="services">
      <h3>Services we offer:</h3>
      <div class="dots"></div>
      <ul>
        <li>Accounting and Taxation</li>
        <li>Corporate and Business Advice</li>
        <li>Family Wealth Management</li>
        <li>Audit and Assurance</li>
        <li>Self Managed Super Fund<br>Administration</li>
      </ul>
    </aside>
  </main>

  <span class="fold left"></span>
  <span class="fold right"></span>
  <footer class="footer">
    <ul class="footer-links">
      <li>Home</li><li>About us</li><li>Careers</li><li>Newsletter</li><li>Contact Us</li>
    </ul>
    <span class="copyright">© 2011 Corvantis Group. All Right Reserved</span>
  </footer>
</div>
</body>
</html>
```